Tallow Crest Partners Inc. - Marketing Materials (inserts for folder or electronic attachement)

I’m looking for 1-2 one page marketing pieces that will help market the services of Tallow Crest Partners Inc. (TCP). This is not a flyer per se. Rather something that I see as being used in a folder for prospective clients (even existing clients), “leave-behinds”, direct mail or emails to introduce them to the services of TCP and why they should choose our shop over the many others out there. I would like the marketing pieces to be adaptable over time, so that as the business environment changes, content in the pieces can be updated.
A little more about Tallow Crest Partners Inc.: TCP is an Alberta (Edmonton area) based Group Benefits Advisory/Consulting firm with a national reach. We are a boutique consulting shop specializing in Group Benefits. The principal (Derek Halvorsen) has been in the industry for 20 years and founded Tallow Crest Partners Inc., with the intent of providing clients "a different type of advisor/broker experience" and giving clients in the Alberta and the Canadian marketplace a better option. Leveraging experience and relationships, TCP's Value Proposition is to provide clients with expert and unbiased advice that will help implement the best program for their specific needs, all while ensuring maximum value. We provide customers a customized experience (no “one size fits all”) and a personalized service model. We focus in the Group Benefits arena (Extended Health Care, Dental Life and Disability, Health Care Spending Accounts, etc.), and use experts for other areas of insurance (Group RRSP and Individual Life insurance).

Key words and phrases to consider:
- cost vs. value,
- core values (transparency, integrity, honesty)
- impartial/unbiased advice
- fair
- we listen
- every customer is important
- personalized service model
- boutique advice, boutique services
- services that we offer/areas of speciality
- Deal with all major Insurers

Key requirements:

- ‘Professional’ feel to design. It is insurance related, after all.
- In keeping with the company name, the design should be modern.
- Blues, greys, teals and blacks are colours that are important and part of TCP’s existing logo.
- Graphics and/or pictures are acceptable.
- Key words: adaptable, expertise, honest(y), transparent, dependable, boutique, consulting, advice/advisory, value, customized approach, etc.

Ideally, this project would be something that could easily be scalable into other pieces and transition into letterhead/stationary as well.

Thank you.

Target Market(s)

Employers, HR Professionals, C suite execs and business owners with or looking for group benefits (employer sponsored Extended Health Care, Dental, Life and Disability) advice and representation.

Industry/Entity Type

Insurance Broker

Font styles to use
Sans Serif

Colors
33a6d7
85cae6
33b8a4
9d9d9d
5c5c5c
000000
86cfc6
3176b5

Requirements
Must have
• It must convey an air of Trust, Integrity, and of course, be modern looking and "fun". Insurance can be a stuffy field and I'd like to take some of the stuffiness away while maintaining a professional image. Also, this piece should be quickly recognizable and assimilated. That is, it should have information, but also be able to processed quickly.
Nice to have
• Have some "pop". Excite the reader and leave them wanting more.
• Flow charts, diagrams.
Should not have
• It must not be stuffy

```html
<!DOCTYPE html>
<html lang="en">
<head>
<meta charset="utf-8">
<title>Tallow Crest Partners Inc. – Group Benefits Advisory</title>
<link href="https://fonts.googleapis.com/css2?family=Mulish:wght@400;600;800&family=Oswald:wght@400;500&display=swap" rel="stylesheet">
<style>
  :root{
    --blue:#3176b5;
    --sky:#33a6d7;
    --sky-light:#85cae6;
    --teal:#33b8a4;
    --teal-light:#86cfc6;
    --grey:#9d9d9d;
    --ink:#5c5c5c;
    --black:#000000;
    --paper:#f6f8f9;
  }
  *{margin:0;padding:0;box-sizing:border-box}
  html,body{width:869px;height:1200px;overflow:hidden;background:var(--paper)}
  .sheet{position:relative;width:869px;height:1200px;overflow:hidden;
    background:linear-gradient(180deg,#ffffff 0%,var(--paper) 100%);
    font-family:"Mulish",sans-serif;color:var(--black)}
  .art{position:absolute;left:0;top:0}
  .brand{position:absolute;left:520px;top:78px;display:flex;align-items:center;gap:16px;
    font-family:"Mulish",sans-serif;font-weight:800;color:var(--sky)}
  .brand-dot{width:58px;height:58px;border-radius:50%;background:var(--sky)}
  .brand-name{font-size:78px;line-height:.9;letter-spacing:1px}
  .brand-full{display:block;font-size:14.5px;letter-spacing:.6px;margin-top:8px}
  .phone{position:absolute;left:630px;top:266px;width:236px;text-align:center;color:#fff}
  .phone svg{display:block;margin:0 auto}
  .phone-number{font-family:"Oswald",sans-serif;font-weight:500;font-size:28px;line-height:1;margin-top:8px;white-space:nowrap}
  .tab{position:absolute;top:665px;height:31px;color:#fff;
    font-family:"Oswald",sans-serif;font-weight:400;font-size:24px;line-height:31px;
    background:linear-gradient(90deg,var(--sky),var(--teal))}
  .tab-left{left:0;width:192px;padding-left:38px;border-radius:0 16px 16px 0}
  .tab-right{left:628px;width:241px;padding-left:14px;border-radius:16px 0 0 16px}
  .reasons{position:absolute;left:44px;top:714px;list-style:none}
  .reasons li{display:flex;align-items:center;height:25.7px;font-size:11.6px;color:#222}
  .reasons svg{width:11px;height:11px;margin-right:10px;flex:none}
  .about{position:absolute;left:525px;top:712px;width:303px;font-size:11.4px;line-height:20px;
    text-align:justify;color:#222}
  .footer{position:absolute;left:0;top:1127px;width:869px;height:73px;border-radius:0 26px 0 0;
    background:linear-gradient(90deg,var(--blue) 0%,var(--sky) 30%,var(--teal) 60%,var(--sky) 85%,var(--blue) 100%);
    color:#fff;font-weight:600;font-size:13.2px;letter-spacing:.3px}
  .footer-item{position:absolute;top:31px;display:flex;align-items:center;gap:7px}
  .footer-address{left:44px}
  .footer-email{right:41px}
  .footer svg{width:15px;height:15px}
</style>
</head>
<body>
<main class="sheet">

  <svg class="art" width="869" height="1200" viewBox="0 0 869 1200">
    <defs>
      <linearGradient id="photoTone" x1="0" y1="0" x2="1" y2="1">
        <stop offset="0" stop-color="#c9c2b8"/>
        <stop offset=".45" stop-color="#8a6a52"/>
        <stop offset="1" stop-color="#5a4434"/>
      </linearGradient>
      <linearGradient id="networkTone" x1="0" y1="0" x2="1" y2="1">
        <stop offset="0" stop-color="#132a4a"/>
        <stop offset=".55" stop-color="#3a5f8a"/>
        <stop offset="1" stop-color="#0c1d36"/>
      </linearGradient>
      <linearGradient id="accent" x1="0" y1="0" x2="1" y2="1">
        <stop offset="0" stop-color="#3176b5"/>
        <stop offset="1" stop-color="#33b8a4"/>
      </linearGradient>
      <linearGradient id="tabletTone" x1="0" y1="0" x2="1" y2="0">
        <stop offset="0" stop-color="#e9e4df"/>
        <stop offset="1" stop-color="#cfd4d8"/>
      </linearGradient>
      <linearGradient id="chartTone" x1="0" y1="1" x2="1" y2="0">
        <stop offset="0" stop-color="#85cae6"/>
        <stop offset="1" stop-color="#3176b5"/>
      </linearGradient>
    </defs>

    <polygon points="0,0 480,0 480,193 157,526 0,640" fill="url(#photoTone)"
      role="img" aria-label="Photo: business colleagues bumping fists over a desk with invoices and a newspaper"/>

    <polygon points="493,192 761,452 493,714 226,452" fill="#ffffff"/>
    <polygon points="493,200 751,452 493,706 236,452" fill="url(#networkTone)"
      role="img" aria-label="Photo: hand pointing at a glowing network of connected words"/>

    <polygon points="228,458 308,537 228,616 147,537" fill="url(#accent)"/>
    <polygon points="747,204 866,320 747,434 630,320" fill="url(#accent)"/>

    <rect x="0" y="987" width="206" height="153" fill="url(#tabletTone)"
      role="img" aria-label="Photo: hands holding a tablet showing a business dashboard"/>
    <rect x="224" y="987" width="251" height="153" fill="url(#chartTone)" opacity=".55"
      role="img" aria-label="Illustration: rising arrows growth graphic"/>
  </svg>

  <div class="brand">
    <span class="brand-dot"></span>
    <div>
      <span class="brand-name">TCP</span>
      <span class="brand-full">TALLOW CREST PARTNERS</span>
    </div>
  </div>

  <div class="phone">
    <svg width="36" height="36" viewBox="0 0 42 42" aria-hidden="true">
      <circle cx="21" cy="21" r="20" fill="#fff"/>
      <path d="M15 12c1.5-.8 2.6 1.8 3.2 3.2.5 1.2-1.6 2-1.2 3 1 2.4 2.8 4.2 5 5.2 1 .4 1.8-1.6 3-1.2 1.4.6 4 1.8 3.2 3.2-1 2-3 3-5.2 2.4C17.6 26 14.6 22.6 13 18c-.6-2.2.2-5 2-6z" fill="var(--sky)"/>
    </svg>
    <div class="phone-number">780.555.0148</div>
  </div>

  <h2 class="tab tab-left">WHY CHOOSE US</h2>
  <h2 class="tab tab-right">ABOUT OUR COMPANY</h2>

  <ul class="reasons">
    <li><svg viewBox="0 0 12 12"><circle cx="6" cy="6" r="5" fill="none" stroke="#33a6d7" stroke-width="1.2"/><path d="M3.5 6l2 2 4-4" fill="none" stroke="#33b8a4" stroke-width="1.4"/></svg>Cost vs. value,</li>
    <li><svg viewBox="0 0 12 12"><circle cx="6" cy="6" r="5" fill="none" stroke="#33a6d7" stroke-width="1.2"/><path d="M3.5 6l2 2 4-4" fill="none" stroke="#33b8a4" stroke-width="1.4"/></svg>Core values (transparency, integrity, honesty)</li>
    <li><svg viewBox="0 0 12 12"><circle cx="6" cy="6" r="5" fill="none" stroke="#33a6d7" stroke-width="1.2"/><path d="M3.5 6l2 2 4-4" fill="none" stroke="#33b8a4" stroke-width="1.4"/></svg>Impartial/unbiased advice</li>
    <li><svg viewBox="0 0 12 12"><circle cx="6" cy="6" r="5" fill="none" stroke="#33a6d7" stroke-width="1.2"/><path d="M3.5 6l2 2 4-4" fill="none" stroke="#33b8a4" stroke-width="1.4"/></svg>Fair</li>
    <li><svg viewBox="0 0 12 12"><circle cx="6" cy="6" r="5" fill="none" stroke="#33a6d7" stroke-width="1.2"/><path d="M3.5 6l2 2 4-4" fill="none" stroke="#33b8a4" stroke-width="1.4"/></svg>We listen</li>
    <li><svg viewBox="0 0 12 12"><circle cx="6" cy="6" r="5" fill="none" stroke="#33a6d7" stroke-width="1.2"/><path d="M3.5 6l2 2 4-4" fill="none" stroke="#33b8a4" stroke-width="1.4"/></svg>Every customer is important</li>
    <li><svg viewBox="0 0 12 12"><circle cx="6" cy="6" r="5" fill="none" stroke="#33a6d7" stroke-width="1.2"/><path d="M3.5 6l2 2 4-4" fill="none" stroke="#33b8a4" stroke-width="1.4"/></svg>Personalized service model</li>
    <li><svg viewBox="0 0 12 12"><circle cx="6" cy="6" r="5" fill="none" stroke="#33a6d7" stroke-width="1.2"/><path d="M3.5 6l2 2 4-4" fill="none" stroke="#33b8a4" stroke-width="1.4"/></svg>Boutique advice, boutique services</li>
    <li><svg viewBox="0 0 12 12"><circle cx="6" cy="6" r="5" fill="none" stroke="#33a6d7" stroke-width="1.2"/><path d="M3.5 6l2 2 4-4" fill="none" stroke="#33b8a4" stroke-width="1.4"/></svg>Services that we offer/areas of speciality</li>
    <li><svg viewBox="0 0 12 12"><circle cx="6" cy="6" r="5" fill="none" stroke="#33a6d7" stroke-width="1.2"/><path d="M3.5 6l2 2 4-4" fill="none" stroke="#33b8a4" stroke-width="1.4"/></svg>Deal with all major Insurers</li>
  </ul>

  <p class="about">We are a boutique consulting shop specializing in Group Benefits. The principal (Derek Halvorsen) has been in the industry for 20 years and founded Tallow Crest Partners Inc., with the intent of providing clients "a different type of advisor/broker experience" and giving clients in the Alberta and the Canadian marketplace a better option. Leveraging experience and relationships, TCP's Value Proposition is to provide clients with expert and unbiased advice that will help implement the best program for their specific needs, all while ensuring maximum value. We provide customers a customized experience (no “one size fits all”) and a personalized service model. We focus in the Group Benefits arena (Extended Health Care, Dental Life and Disability, Health Care Spending Accounts, etc.), and use experts for other areas of insurance (Group RRSP and Individual Life insurance).</p>

  <footer class="footer">
    <div class="footer-item footer-address">
      <svg viewBox="0 0 16 16" aria-hidden="true"><circle cx="8" cy="8" r="7.5" fill="#fff"/><path d="M8 3.5a3 3 0 0 0-3 3c0 2.2 3 5.5 3 5.5s3-3.3 3-5.5a3 3 0 0 0-3-3z" fill="var(--sky)"/><circle cx="8" cy="6.5" r="1.1" fill="#fff"/></svg>
      4410 JUNIPER RIDGE RD., EDMONTON, AB T5K 2P9
    </div>
    <div class="footer-item footer-email">
      <svg viewBox="0 0 16 16" aria-hidden="true"><circle cx="8" cy="8" r="7.5" fill="#fff"/><rect x="4" y="5" width="8" height="6" rx="1" fill="var(--sky)"/><path d="M4.3 5.5L8 8.3l3.7-2.8" fill="none" stroke="#fff" stroke-width=".9"/></svg>
      HELLO@TALLOWCREST.CA
    </div>
  </footer>

</main>
</body>
</html>
```